Business cards for Harbourline Supply Pty Ltd that import building products into Australia from China
Target Market(s)
Business to Business
Industry/Entity Type
Business
Contact Information for Business Card
Front: Logo and Business Name
Rear:
Vernon Asquill
General Manager
Mobile: 0427 196 354
email: vern@harbourlinesupply.com.au
alternative email: vern@ochrefield.com.au
web: www.harbourlinesupply.com.au
Geelong, Cairns and Fremantle
Colors
ec1f27
fbee3d

```html
<!DOCTYPE html>
<html lang="en">
<head>
<meta charset="utf-8">
<title>Harbourline Supply – Business Cards</title>
<link rel="stylesheet" href="https://fonts.googleapis.com/css2?family=Montserrat:wght@400;500;700&display=swap">
<style>
  :root {
    --backdrop: #333333;
    --card-dark: #161616;
    --card-light: #f1f1f1;
    --brand-red: #ec1f27;
    --ink: #1c1c1c;
    --ink-soft: #3a3a3a;
    --rule: #555555;
    --white: #ffffff;
  }
  * { box-sizing: border-box; margin: 0; padding: 0; }
  html, body {
    width: 1200px; height: 750px; overflow: hidden;
    background: var(--backdrop);
    font-family: "Montserrat", sans-serif;
  }
  .stage {
    width: 1200px; height: 750px;
    display: flex; align-items: center; justify-content: center; gap: 60px;
  }
  .card {
    width: 500px; height: 290px; position: relative; overflow: hidden;
    box-shadow: 0 20px 40px rgba(0,0,0,.35);
  }

  /* Front */
  .card--front {
    background: var(--card-dark);
    display: flex; flex-direction: column; align-items: center; justify-content: center;
  }
  .brand { display: flex; align-items: center; gap: 10px; }
  .brand__dot {
    width: 14px; height: 14px; border-radius: 50%; background: var(--brand-red);
  }
  .brand__name {
    font-weight: 700; font-size: 36px; letter-spacing: .5px; color: var(--white);
  }
  .front__tagline {
    margin-top: 8px; color: var(--brand-red);
    font-size: 13px; letter-spacing: 3px;
  }

  /* Back */
  .card--back { background: var(--card-light); }
  .card--back .brand { position: absolute; left: 30px; top: 34px; }
  .card--back .brand__name { color: var(--ink); font-size: 24px; }
  .card--back .brand__dot { width: 10px; height: 10px; }
  .back__rule {
    position: absolute; left: 30px; right: 30px; top: 94px;
    height: 1px; background: var(--rule);
  }
  .back__band {
    position: absolute; left: 0; right: 0; bottom: 0; height: 16px;
    background: var(--brand-red);
  }
  .contact-list {
    list-style: none; position: absolute; left: 30px;
    font-size: 11px; color: var(--ink-soft); line-height: 1.45;
  }
  .contact-list--top { top: 108px; }
  .contact-list--bottom { bottom: 34px; }
  .contact-list li { display: flex; gap: 8px; align-items: flex-start; margin-bottom: 3px; }
  .contact-list svg { width: 11px; height: 11px; flex: none; margin-top: 2px; }
  .person {
    position: absolute; right: 30px; top: 150px; text-align: right;
  }
  .person__name {
    color: var(--brand-red); font-weight: 700; font-size: 14px; letter-spacing: .5px;
    text-transform: uppercase;
  }
  .person__title { font-size: 12px; color: var(--ink-soft); }
</style>
</head>
<body>
<main class="stage">
  <section class="card card--front" aria-label="Card front">
    <div class="brand">
      <span class="brand__dot"></span>
      <span class="brand__name">Harbourline Supply</span>
    </div>
    <p class="front__tagline">Geelong, Cairns and Fremantle</p>
  </section>

  <section class="card card--back" aria-label="Card back">
    <div class="brand">
      <span class="brand__dot"></span>
      <span class="brand__name">Harbourline Supply</span>
    </div>
    <div class="back__rule"></div>

    <ul class="contact-list contact-list--top">
      <li>
        <svg viewBox="0 0 12 12"><rect x="3" y="1" width="6" height="10" rx="1" fill="none" stroke="#ec1f27" stroke-width="1.2"/></svg>
        <span>0427 196 354</span>
      </li>
      <li>
        <svg viewBox="0 0 12 12"><circle cx="6" cy="6" r="4.2" fill="none" stroke="#ec1f27" stroke-width="1.6"/></svg>
        <span>42 Wharf Street<br>Geelong VIC 3220</span>
      </li>
    </ul>

    <div class="person">
      <p class="person__name">Vernon Asquill</p>
      <p class="person__title">General Manager</p>
    </div>

    <ul class="contact-list contact-list--bottom">
      <li>
        <svg viewBox="0 0 12 12"><rect x="1" y="2.5" width="10" height="7" fill="#ec1f27"/></svg>
        <span>vern@harbourlinesupply.com.au</span>
      </li>
      <li>
        <svg viewBox="0 0 12 12"><rect x="1" y="2.5" width="10" height="7" fill="#ec1f27"/></svg>
        <span>vern@ochrefield.com.au</span>
      </li>
      <li>
        <svg viewBox="0 0 12 12"><circle cx="6" cy="6" r="5" fill="#ec1f27"/><path d="M1 6h10M6 1c2 2.5 2 7.5 0 10M6 1c-2 2.5-2 7.5 0 10" stroke="#fff" stroke-width=".8" fill="none"/></svg>
        <span>www.harbourlinesupply.com.au</span>
      </li>
    </ul>

    <div class="back__band"></div>
  </section>
</main>
</body>
</html>
```